Business Card For Video Production Company

Please NOTE: I've added some info to the must haves that I should have included at the start. Thank you.

I need a business card design for my video production company based in Orlando called Caldera Film Works. Our work consists of web video marketing (web videos), training videos, sales videos, conference and seminar video production...basically a lot of corporate based work.

We work with successful small businesses, not-for-profits and some Fortune 500 type groups. We bring a lot of knowledge, experience and attention to detail to every project.

I'd like something that communicates strength, confidence, integrity, as well as creative vision. I want to stay away from the standard icons of the media and film industry. I'd like to emphasize the colors of my logo, and also the colors of my website which has a white background. Simple is good.

Our budgets are moderate...generally $1500 to $5000.

www.calderafilm.tv

PS...We don't do weddings or recitals, or that type of production.
Updates

I want to thank all the designers for your updates. There's way too many to be able to give feedback on for all. I hope you understand that. But wow…there are so many great designs everyone has offered. I can't thank you enough…each and everyone. I hope to make my decision soon. I'm not accepting anymore designs from new designers. Brent-

Target Market(s)

Successful small businesses, marketing directors, corporate communication directors, training and human resources professionals. forward thinking not-for profits. Since my company is based in Central Florida, most of my work comes from this area too.

Industry/Entity Type

Marketing

Requirements
Must have
• website address, www.calderafilm.tv
phone number, 407-552-9031
email address, brent@calderafilm.tv

Title
Brent Caldera
Owner/Creative Director

I'd like to have a single line that goes across illustrating our services, maybe separated with bullet points:

Marketing Videos, Corporate Videos, Conference & Seminar Video Production
Should not have
• No film or video icons.
No need to pull language or copy from my website.

```html
<!DOCTYPE html>
<html lang="en">
<head>
<meta charset="utf-8">
<title>Caldera Film Works – Business Card</title>
<link rel="stylesheet" href="https://fonts.googleapis.com/css2?family=Montserrat:wght@700&family=Arimo:wght@700&family=Libre+Baskerville&display=swap">
<style>
  :root {
    --backdrop: #060808;
    --card: #ffffff;
    --brand-blue: #3db0f7;
    --mark-light: #9ff0f7;
    --ink-dark: #3f464b;
    --ink-black: #111111;
  }
  * { margin: 0; padding: 0; box-sizing: border-box; }
  html, body {
    width: 1200px;
    height: 900px;
    overflow: hidden;
    background: var(--backdrop);
  }
  .canvas {
    position: relative;
    width: 1200px;
    height: 900px;
  }
  .card {
    position: absolute;
    width: 580px;
    height: 330px;
    background: var(--card);
    overflow: hidden;
  }
  .card--front { left: 280px; top: 90px; }
  .card--back  { left: 415px; top: 490px; }

  .brand {
    position: absolute;
    display: flex;
    align-items: center;
    gap: 12px;
    font-family: "Montserrat", sans-serif;
    font-weight: 700;
    color: var(--ink-dark);
    white-space: nowrap;
  }
  .brand__square {
    display: block;
    background: var(--brand-blue);
  }
  .card--front .brand { left: 110px; top: 128px; font-size: 31px; }
  .card--front .brand__square { width: 44px; height: 44px; }

  .front__band {
    position: absolute;
    left: 0;
    top: 190px;
    width: 100%;
    height: 28px;
    background: var(--brand-blue);
  }

  .back__bar {
    position: absolute;
    left: 45px;
    width: 88px;
    background: var(--brand-blue);
  }
  .back__bar--upper { top: 0; height: 188px; }
  .back__bar--lower { top: 224px; height: 106px; }

  .holder {
    position: absolute;
    left: 345px;
    top: 58px;
    font-family: "Arimo", sans-serif;
    font-weight: 700;
    font-size: 17px;
    line-height: 22px;
    color: var(--brand-blue);
  }
  .holder__title { display: block; padding-left: 2px; }

  .card--back .brand { left: 150px; top: 135px; font-size: 22px; gap: 9px; }
  .card--back .brand__square { width: 30px; height: 30px; }

  .contact {
    position: absolute;
    left: 152px;
    top: 178px;
    list-style: none;
    font-family: "Libre Baskerville", serif;
    font-size: 12px;
    line-height: 17px;
    color: var(--ink-black);
  }
</style>
</head>
<body>
<main class="canvas">
  <section class="card card--front" aria-label="Card front">
    <div class="front__band"></div>
    <div class="brand"><span class="brand__square"></span>Caldera Film Works</div>
  </section>

  <section class="card card--back" aria-label="Card back">
    <div class="back__bar back__bar--upper"></div>
    <div class="back__bar back__bar--lower"></div>
    <p class="holder">
      <span class="holder__name">Brent Caldera</span><br>
      <span class="holder__title">Owner/Creative Director</span>
    </p>
    <div class="brand"><span class="brand__square"></span>Caldera Film Works</div>
    <ul class="contact">
      <li>website address - www.calderafilm.tv</li>
      <li>phone number - 407-552-9031</li>
      <li>email address - brent@calderafilm.tv</li>
    </ul>
  </section>
</main>
</body>
</html>
```